Stationary design for boutique production house

We need a stationary design for our production house, 'Lorin Studios' based in Singapore. We produce microfilms as well as podcasts, talkshows and events. Our logo is a stylized icon of our director, who is also the executive producer and host of our programs, Lorin. Our main company colors are Red, Black and white. We would like a clean, minimalist design incorporating our existing company logo that conveys a sense of urbanism and elegance.

Logo and font files are attached. f

Target Market(s)

We focus on lifestyle media rather than entertainment.

Industry/Entity Type

Boutique

Font styles to use
Serif
Sans Serif

Colors
ec1f27
ffffff
000000

Requirements
Must have
• Our company logo and at least one of our company colors.
Nice to have
• Our address and contact information.
Should not have
• Changes made to the company logo (using only certain parts of it is fine though)

```html
<!DOCTYPE html>
<html lang="en">
<head>
<meta charset="utf-8">
<title>Lorin Studios — Stationery</title>
<link rel="stylesheet" href="https://fonts.googleapis.com/css2?family=Old+Standard+TT:wght@400;700&family=Arimo:wght@400&display=swap">
<style>
  :root {
    --red: #c0161f;
    --red-bright: #ec1f27;
    --red-deep: #8a1218;
    --black: #111111;
    --white: #ffffff;
    --paper: #f1f1f1;
    --backdrop: #e9e3d3;
    --serif: "Old Standard TT", Georgia, serif;
    --sans: "Arimo", Arial, sans-serif;
  }
  * { box-sizing: border-box; margin: 0; padding: 0; }
  html, body { width: 1200px; height: 1118px; overflow: hidden; }
  body { background: var(--backdrop); position: relative; font-family: var(--serif); color: var(--black); }

  .sheet { position: absolute; background: var(--paper); box-shadow: 0 2px 6px rgba(0,0,0,.18); overflow: hidden; }

  /* Letterhead */
  .letterhead { left: 512px; top: 170px; width: 548px; height: 778px; }
  .letterhead__band { position: absolute; left: 0; top: 0; width: 100%; height: 110px; background: linear-gradient(90deg, var(--red), #d63a44); border-bottom: 4px solid var(--black); }
  .letterhead__name { position: absolute; left: 58px; top: 36px; color: var(--white); font-size: 22px; font-weight: 700; display: flex; align-items: center; gap: 8px; }
  .letterhead__address { position: absolute; left: 348px; top: 34px; color: var(--white); font-size: 11.5px; line-height: 1.35; }
  .letterhead__address .phone { font-family: var(--sans); font-size: 10px; display: block; margin-top: 3px; }

  /* Envelope */
  .envelope { left: 70px; top: 300px; width: 620px; height: 280px; }
  .envelope__flap { position: absolute; left: 0; top: 40px; width: 100%; height: 6px; background: var(--red-deep); }
  .envelope__name { position: absolute; left: 70px; top: 120px; font-size: 30px; font-weight: 700; display: flex; align-items: center; gap: 12px; }
  .envelope__band { position: absolute; left: 0; bottom: 0; width: 100%; height: 56px; background: var(--red); border-top: 6px solid var(--black); }
  .envelope__address { position: absolute; left: 56px; bottom: 14px; color: var(--white); font-size: 16px; letter-spacing: .3px; }

  .dot { display: inline-block; width: 12px; height: 12px; border-radius: 50%; background: var(--red-bright); }
  .dot--small { width: 8px; height: 8px; }
  .dot--white { background: var(--white); }

  /* Business cards */
  .card { position: absolute; width: 252px; height: 148px; box-shadow: 0 2px 5px rgba(0,0,0,.25); }
  .card svg { position: absolute; inset: 0; }
  .card--front { left: 208px; top: 616px; }
  .card--back { left: 208px; top: 800px; }
  .card__content { position: absolute; inset: 0; display: flex; flex-direction: column; align-items: center; }
  .card--front .card__name { margin-top: 40px; font-size: 15px; font-weight: 700; display: flex; align-items: center; gap: 6px; }
  .card__rule { width: 180px; height: 1px; background: var(--black); margin: 10px 0 6px; }
  .card__details { font-size: 7px; line-height: 1.45; text-align: center; }
  .card__details .phone { font-family: var(--sans); }
  .card--back .card__name { margin-top: 62px; font-size: 17px; font-weight: 700; color: var(--white); display: flex; align-items: center; gap: 7px; }
</style>
</head>
<body>

<section class="sheet letterhead" aria-label="Letterhead">
  <div class="letterhead__band">
    <div class="letterhead__name"><span class="dot dot--white"></span>Lorin Studios</div>
    <p class="letterhead__address">18 Kallang Way,<br>Harbour Works Building,<br>#04 12, Singapore 349210<span class="phone">+65 6100 4827</span></p>
  </div>
</section>

<section class="sheet envelope" aria-label="Envelope">
  <div class="envelope__flap"></div>
  <div class="envelope__name"><span class="dot"></span>Lorin Studios</div>
  <div class="envelope__band">
    <p class="envelope__address">18 Kallang Way, Harbour Works Building, #04 12, Singapore 349210</p>
  </div>
</section>

<section class="card card--front" aria-label="Business card front">
  <svg width="252" height="148" viewBox="0 0 252 148">
    <rect width="252" height="148" fill="var(--red)"/>
    <path d="M30 0 H222 Q248 74 222 148 H30 Q4 74 30 0 Z" fill="var(--paper)" stroke="var(--black)" stroke-width="2"/>
  </svg>
  <div class="card__content">
    <div class="card__name"><span class="dot dot--small"></span>Lorin Studios</div>
    <div class="card__rule"></div>
    <p class="card__details"><span class="phone">+65 6100 4827</span><br>hello@lorinstudios.sg<br>18 Kallang Way, Harbour Works Building,<br>Singapore 349210</p>
  </div>
</section>

<section class="card card--back" aria-label="Business card back">
  <svg width="252" height="148" viewBox="0 0 252 148">
    <rect width="252" height="148" fill="var(--black)"/>
    <path d="M0 30 H20 Q38 90 26 148 H0 Z" fill="var(--red)"/>
    <path d="M252 0 H226 Q214 50 236 118 H252 Z" fill="var(--red)"/>
  </svg>
  <div class="card__content">
    <div class="card__name"><span class="dot dot--small dot--white"></span>Lorin Studios</div>
  </div>
</section>

</body>
</html>
```